International Food Manufacturer in the need of a new business card and logo.

Our Company - Northgate Pantry Ltd.

Our Industry - Food and Drink

We are a Wild Harvested Food Distributor / Manufacturer. We service the following food sectors: Supermarkets, Hotels, Restaurants, Cafes, Catering and all people looking to eat healthy food products.

Slogan - The foremost source for everything healthy

Business card details -

48-52 Marlow Lane
Hatherby Green
London
EC9Z 4RT United Kingdom
Dennis Prowle
+44 7000 481736 - UK
+971 50 7739205 - UAE
+38 063 914 2758 - Ukraine
dennis@northgatepantry.example
www.northgatepantry.example

Goal - We are looking for a dynamic modern new look for our corporate image and a designer who can bring this new concept to our future food product designs. Please try to incorporate 3d hexagonal vector Imaging in your design concepts.

Target Market(s)

Industry/Entity Type

Food Service

Contact Information for Business Card

Northgate Pantry Ltd.
48-52 Marlow Lane
Hatherby Green
London
EC9Z 4RT United Kingdom
Dennis Prowle
+44 7000 481736 - UK
+971 50 7739205 - UAE

Font styles to use
Serif

Colors

Designer to choose colors to be used in the design.

Requirements
Must have
• Please read project description above.
Nice to have
Should not have

```html
<!DOCTYPE html>
<html lang="en">
<head>
<meta charset="utf-8">
<title>Northgate Pantry Ltd. – Business Card and Logo</title>
<link rel="stylesheet" href="https://fonts.googleapis.com/css2?family=Open+Sans:wght@400;600&display=swap">
<style>
  :root {
    --brand-navy: #1c5a80;
    --brand-deep: #1a4d72;
    --brand-bright: #1a9ad6;
    --brand-sky: #3fb4e8;
    --paper: #ffffff;
    --stage: #eef1f4;
    --ink: #2f3236;
    --rule: #c9ced4;
  }
  * { box-sizing: border-box; margin: 0; padding: 0; }
  html, body {
    width: 1200px; height: 1200px; overflow: hidden;
    background: var(--paper);
    font-family: "Open Sans", Arial, sans-serif;
    color: var(--ink);
  }
  .canvas { position: relative; width: 1200px; height: 1200px; }

  /* Card presentation area */
  .card-stage {
    position: absolute; left: 0; top: 0; width: 1200px; height: 800px;
    background: var(--stage);
    border-bottom: 2px solid var(--rule);
  }
  .card {
    position: absolute; width: 520px; height: 300px;
    border-radius: 0 18px 0 18px;
    overflow: hidden;
    box-shadow: 0 10px 28px rgba(20, 50, 80, 0.18);
  }

  /* Front of card */
  .card-front { left: 50px; top: 250px; background: var(--brand-navy); }
  .card-front .identity-panel {
    position: absolute; left: 0; top: 0; width: 190px; height: 300px;
    background: var(--paper);
    padding: 26px 20px;
    display: flex; flex-direction: column; justify-content: space-between;
  }
  .holder-name {
    font-size: 15px; font-weight: 600; color: var(--ink);
  }
  .holder-name::before {
    content: ""; display: inline-block; width: 4px; height: 4px;
    background: var(--brand-bright); margin-right: 6px; vertical-align: middle;
  }
  .card-wordmark {
    display: flex; align-items: center; gap: 8px;
    font-size: 15px; font-weight: 600; color: var(--brand-navy); line-height: 1.2;
  }
  .card-wordmark .mark-dot {
    width: 14px; height: 14px; border-radius: 50%; background: var(--brand-navy); flex: none;
  }
  .card-front .texture {
    position: absolute; left: 190px; bottom: 0; width: 330px; height: 70px;
    background: linear-gradient(0deg, rgba(63,180,232,0.28), rgba(63,180,232,0));
  }
  .contact-list {
    position: absolute; left: 176px; top: 26px; right: 20px;
    list-style: none; color: var(--paper);
  }
  .contact-item {
    display: flex; gap: 16px; margin-bottom: 14px;
    font-size: 12.5px; line-height: 1.45;
  }
  .contact-icon {
    flex: none; width: 28px; height: 28px; border-radius: 5px;
    background: var(--brand-bright);
    display: flex; align-items: center; justify-content: center;
  }
  .contact-icon svg { width: 16px; height: 16px; }

  /* Back of card */
  .card-back {
    left: 630px; top: 250px;
    background: radial-gradient(circle at 62% 40%, var(--brand-sky) 0%, #1a86c0 45%, var(--brand-deep) 100%);
  }
  .card-back .texture {
    position: absolute; left: 0; top: 0; width: 110px; height: 300px;
    background: linear-gradient(90deg, rgba(63,180,232,0.55), rgba(63,180,232,0));
  }
  .card-back .back-wordmark {
    position: absolute; left: 0; right: 0; top: 0; bottom: 0;
    display: flex; align-items: center; justify-content: center; gap: 10px;
    font-size: 22px; font-weight: 600; color: var(--paper);
  }
  .card-back .mark-dot {
    width: 22px; height: 22px; border-radius: 50%; background: var(--paper);
  }

  /* Logo lockup */
  .logo-lockup {
    position: absolute; left: 0; top: 800px; width: 1200px; height: 400px;
    display: flex; align-items: center; justify-content: center; gap: 36px;
  }
  .logo-lockup .mark-circle {
    width: 200px; height: 200px; border-radius: 50%; background: var(--brand-navy);
  }
  .logo-lockup .lockup-name {
    font-size: 72px; font-weight: 600; color: var(--brand-navy); line-height: 1.1;
  }
</style>
</head>
<body>
<main class="canvas">

  <section class="card-stage" aria-label="Business card front and back">

    <article class="card card-front">
      <div class="texture" role="img" aria-label="Decorative square mosaic pattern in light blue"></div>
      <div class="identity-panel">
        <p class="holder-name">Dennis Prowle</p>
        <p class="card-wordmark"><span class="mark-dot"></span>Northgate Pantry Ltd.</p>
      </div>
      <ul class="contact-list">
        <li class="contact-item">
          <span class="contact-icon">
            <svg viewBox="0 0 16 16"><path d="M8 1.5a4.5 4.5 0 0 0-4.5 4.5c0 3.3 4.5 8.5 4.5 8.5s4.5-5.2 4.5-8.5A4.5 4.5 0 0 0 8 1.5z" fill="#fff"/><circle cx="8" cy="6" r="1.7" fill="#1a9ad6"/></svg>
          </span>
          <span>48-52 Marlow Lane<br>Hatherby Green<br>London<br>EC9Z 4RT United Kingdom</span>
        </li>
        <li class="contact-item">
          <span class="contact-icon">
            <svg viewBox="0 0 16 16"><path d="M4 1.5l2.2 2.6-1.3 1.6c.8 1.9 2.2 3.3 4.1 4.2l1.6-1.3 2.6 2.2-1.2 2.4C7 12.9 3.1 9 2.1 3.3z" fill="#fff"/></svg>
          </span>
          <span>+44 7000 481736 - UK<br>+971 50 7739205 - UAE<br>+38 063 914 2758 - Ukraine</span>
        </li>
        <li class="contact-item">
          <span class="contact-icon">
            <svg viewBox="0 0 16 16"><rect x="1.5" y="3.5" width="13" height="9" rx="1" fill="none" stroke="#fff" stroke-width="1.4"/><path d="M2 4l6 5 6-5" fill="none" stroke="#fff" stroke-width="1.4"/></svg>
          </span>
          <span>dennis@northgatepantry.example</span>
        </li>
        <li class="contact-item">
          <span class="contact-icon">
            <svg viewBox="0 0 16 16"><circle cx="8" cy="8" r="6.2" fill="none" stroke="#fff" stroke-width="1.3"/><ellipse cx="8" cy="8" rx="2.8" ry="6.2" fill="none" stroke="#fff" stroke-width="1.1"/><path d="M1.8 8h12.4" stroke="#fff" stroke-width="1.1"/></svg>
          </span>
          <span>www.northgatepantry.example</span>
        </li>
      </ul>
    </article>

    <article class="card card-back">
      <div class="texture" role="img" aria-label="Decorative square mosaic pattern fading from the left edge"></div>
      <p class="back-wordmark"><span class="mark-dot"></span>Northgate Pantry Ltd.</p>
    </article>

  </section>

  <section class="logo-lockup" aria-label="Company logo">
    <span class="mark-circle"></span>
    <p class="lockup-name">Northgate Pantry Ltd.</p>
  </section>

</main>
</body>
</html>
```